Marlbrook Crest Healthcare Needs a Business Card Design

We need a business card design for a company based in Shorewood IL called "Marlbrook Crest Healthcare". We provide an integrated medical model involving chiropractic, trigger point injections and other medical services in one location. I have attached our logo to this with the colors being in the puzzle design of the logo. We are looking for a great design that will WOW those around us but also be able to communicate our information easily

Industry/Entity Type

Medical

Contact Information for Business Card

This is a integrated Medical office featuring numerous services to clients in the office.

Requirements
Must have
• Logo

```html
<!DOCTYPE html>
<html lang="en">
<head>
<meta charset="utf-8">
<title>Marlbrook Crest Healthcare – Business Card</title>
<link rel="stylesheet" href="https://fonts.googleapis.com/css2?family=Exo+2:wght@400;500&display=swap">
<style>
  :root {
    --stage: #2a2a2c;
    --card-white: #ffffff;
    --ink: #2b2b2b;
    --accent-orange: #f08a24;
    --brand-blue: #3a7fc1;
    --pastel-blue: #cfe4f6;
    --pastel-lilac: #d6d0ea;
    --pastel-green: #d3ead2;
    --pastel-peach: #fbdcc4;
    --rule: #3a3a3a;
  }
  * { box-sizing: border-box; margin: 0; padding: 0; }
  html, body { width: 1200px; height: 754px; overflow: hidden; }
  body {
    background: var(--stage);
    font-family: "Exo 2", sans-serif;
    position: relative;
  }
  .card {
    position: absolute;
    top: 222px;
    width: 520px;
    height: 310px;
    box-shadow: 0 6px 18px rgba(0,0,0,0.45);
    overflow: hidden;
  }
  .card--back { left: 55px; }
  .card--front { left: 625px; background: var(--card-white); }

  .card__wash {
    position: absolute; inset: 0;
    background:
      radial-gradient(circle at 12% 18%, var(--pastel-blue) 0, transparent 55%),
      radial-gradient(circle at 80% 10%, var(--pastel-lilac) 0, transparent 55%),
      radial-gradient(circle at 88% 70%, var(--pastel-green) 0, transparent 55%),
      radial-gradient(circle at 25% 92%, var(--pastel-peach) 0, transparent 58%),
      linear-gradient(135deg, var(--pastel-blue), var(--pastel-lilac) 45%, var(--pastel-green) 65%, var(--pastel-peach));
  }
  .contact {
    position: absolute;
    left: 190px;
    top: 62px;
    color: var(--ink);
  }
  .contact__name {
    color: var(--accent-orange);
    font-size: 15px;
    font-weight: 500;
    letter-spacing: 0.5px;
    text-transform: uppercase;
  }
  .contact__title {
    font-size: 10px;
    letter-spacing: 0.6px;
    text-transform: uppercase;
    margin-top: 2px;
  }
  .contact__list { list-style: none; margin-top: 22px; }
  .contact__item {
    display: flex; align-items: center; gap: 6px;
    font-size: 11px; letter-spacing: 0.3px;
    margin-bottom: 6px;
  }
  .icon { width: 12px; height: 12px; flex: none; }
  .address {
    position: absolute;
    left: 230px; top: 214px;
    width: 220px;
    border-top: 1px solid var(--rule);
    padding-top: 34px;
    display: flex; align-items: center; gap: 6px;
    font-size: 10.5px; color: var(--ink); letter-spacing: 0.2px;
  }

  .brand {
    position: absolute;
    left: 50%; top: 50%;
    transform: translate(-50%, -50%);
    display: flex; align-items: center; gap: 10px;
    color: var(--brand-blue);
    font-size: 22px;
    font-weight: 500;
    letter-spacing: 0.5px;
    white-space: nowrap;
  }
  .brand__mark { width: 34px; height: 34px; background: var(--accent-orange); flex: none; }
</style>
</head>
<body>
  <section class="card card--back">
    <div class="card__wash" role="img" aria-label="Soft pastel backdrop in the brand's blue, lilac, green and peach tones"></div>
    <div class="contact">
      <p class="contact__name">Daniel Hartwell</p>
      <p class="contact__title">General Manager</p>
      <ul class="contact__list">
        <li class="contact__item">
          <svg class="icon" viewBox="0 0 12 12"><circle cx="6" cy="6" r="6" fill="#f08a24"/><path d="M4 3.2l1 1.2-.6.7c.4.9 1 1.5 1.9 1.9l.7-.6 1.2 1-.6.9C5.6 8 4 6.4 3.2 4.4z" fill="#fff"/></svg>
          012 555 0148
        </li>
        <li class="contact__item">
          <svg class="icon" viewBox="0 0 12 12"><circle cx="6" cy="6" r="6" fill="#f08a24"/><rect x="3" y="4" width="6" height="4" fill="#fff"/><path d="M3 4l3 2.2L9 4" stroke="#f08a24" stroke-width="0.7" fill="none"/></svg>
          hello@marlbrookcrest.com
        </li>
        <li class="contact__item">
          <svg class="icon" viewBox="0 0 12 12"><circle cx="6" cy="6" r="6" fill="#f08a24"/><circle cx="6" cy="6" r="3" fill="none" stroke="#fff" stroke-width="0.8"/><path d="M3 6h6M6 3v6" stroke="#fff" stroke-width="0.6"/></svg>
          www.marlbrookcrest.com
        </li>
      </ul>
    </div>
    <div class="address">
      <svg class="icon" viewBox="0 0 12 12"><circle cx="6" cy="6" r="6" fill="#f08a24"/><path d="M6 2.5a2 2 0 0 1 2 2c0 1.5-2 4-2 4s-2-2.5-2-4a2 2 0 0 1 2-2z" fill="#fff"/></svg>
      214 4th floor,Crest Avenue Road MBK
    </div>
  </section>

  <section class="card card--front">
    <div class="brand">
      <span class="brand__mark"></span>
      <span class="brand__name">Marlbrook Crest Healthcare</span>
    </div>
  </section>
</body>
</html>
```